Innovative biopolymers technology company needs a professional and engaging website

KELVO Polymer Systems AG is a biopolymer technology licensing company that enables plastic compounders to access new markets and innovate, plastic converters to manufacture bio-based, biodegradable, and bio-neutral plastic, and brand owners to satisfy the end-users’ demand for ‘greener’ plastics.

Our purpose is to help mankind ‘enjoy the convenience of plastic products guilt-free’. That’s why we’ve developed and patented our MARUSTEN® Technology, which enables producing plastics that are ‘kind at heart’. Our products are based on renewable materials, up to 99%, and can be – if required – 100% biodegradable at the same time.

Technically our bio plastics could replace 90% of today’s polyethylene applications. Therefore, our vision is ‘to make MARUSTEN® the world’s standard for the production and innovation in the area of biopolymers’.

We'd like to see website designs that portray us a serious technology company, whose products benefit the environment and brings alive our brand promise of 'kind at heart'.

Target Market(s)

Our primary target audience are plastics compounders that either want to produce resin/pellets, which allow their clients to produce either bio-based or biodegradable plastic.

Industry/Entity Type

Biodegradable

Requirements
Must have
• The website should be designed that it creates the desired user experience, represents the pre-defined structure, and meets our brand guidelines (see attached document KELVO_WebsiteDesignBrief_FinalVersion.pdf). Moreover, it needs to include the prepared content (see attached document KELVO_WebsiteContent_FinalVersion.doc).
Nice to have
• Ideally the selected Wordpress template should have an ordering functionality build-in already so that at a later stage we could order a product ordering process.
Should not have
• The design shouldn't look like purely an environmental company.

```html
<!DOCTYPE html>
<html lang="en">
<head>
<meta charset="utf-8">
<title>KELVO Polymer Systems AG – Home</title>
<link href="https://fonts.googleapis.com/css2?family=Open+Sans:wght@300;400;600;700&display=swap" rel="stylesheet">
<style>
:root{
  --green:#76b22c;
  --green-dark:#4e7f1a;
  --teal:#2a8d9c;
  --blue:#1f78b4;
  --ink:#333;
  --muted:#8a8a8a;
  --line:#e2e2e2;
  --footer:#2b2b2b;
  --footer-deep:#1e1e1e;
  --footer-text:#a9a9a9;
  --white:#fff;
}
*{box-sizing:border-box;margin:0;padding:0}
html,body{width:720px;height:1200px;overflow:hidden;background:var(--white)}
body{font-family:"Open Sans",Arial,sans-serif;color:var(--ink);position:relative}
.wrap{width:624px;margin:0 auto;position:relative}

/* header */
.site-header{height:77px;position:relative}
.brand{position:absolute;left:0;top:20px}
.brand-name{display:flex;align-items:center;gap:6px;font-size:26px;font-weight:700;color:var(--green);letter-spacing:1px;line-height:1}
.brand-dot{width:10px;height:10px;border-radius:50%;background:var(--green)}
.brand-tag{font-size:8px;color:var(--muted);margin-top:3px;margin-left:16px}
.topbar{position:absolute;right:0;top:12px;display:flex;align-items:center;gap:8px;font-size:9px;color:var(--muted)}
.topbar .phone{font-size:11px;color:var(--ink);font-weight:600;display:flex;align-items:center;gap:4px}
.topbar .sq{width:9px;height:9px;background:var(--teal);display:inline-block;vertical-align:middle}
.main-nav{position:absolute;right:0;top:47px;display:flex;gap:0;font-size:10.5px}
.main-nav a{color:var(--muted);text-decoration:none;padding:0 8px;border-left:1px solid var(--line)}
.main-nav a:first-child{border-left:none}
.main-nav a.active{color:var(--green)}

/* hero */
.hero{height:278px;position:relative;background:linear-gradient(180deg,#a8cf6a 0%,#5f9a2a 35%,#8fc24c 55%,#3f7d2b 75%,#5c8f3a 100%)}
.hero-caption{position:absolute;left:0;bottom:14px;background:rgba(20,40,20,.55);padding:8px 16px 8px 14px;color:var(--white)}
.hero-caption .kicker{font-size:10px;letter-spacing:.5px}
.hero-caption h2{font-size:19px;font-weight:700;letter-spacing:.3px;line-height:1.15}
.hero-caption .cta{font-size:10px;display:flex;align-items:center;gap:5px;margin-top:2px}

/* welcome */
.welcome{text-align:center;padding-top:22px;height:143px}
.welcome h1{font-size:21px;font-weight:300;color:#555}
.welcome p{font-size:9.5px;color:var(--muted);width:390px;margin:6px auto 0;line-height:1.35}
.btn{display:inline-block;background:var(--teal);color:var(--white);font-size:8px;font-weight:600;padding:4px 12px;margin-top:10px;border-radius:2px;letter-spacing:.4px}

/* feature cards */
.features{display:flex;gap:16px;height:160px}
.card{width:144px}
.card-img{height:84px}
.card h3{font-size:10px;font-weight:700;color:var(--blue);line-height:1.25;margin-top:6px}
.card p{font-size:8.5px;color:var(--muted);line-height:1.35;margin-top:3px}

/* lower */
.lower{display:flex;justify-content:space-between;margin-top:60px;height:260px}
.news{width:390px}
.section-title{font-size:16px;font-weight:400;color:#444;margin-bottom:14px}
.news-item{display:flex;gap:10px;margin-bottom:18px}
.news-thumb{width:46px;height:46px;flex:none}
.news-item h4{font-size:10px;color:var(--blue);font-weight:600}
.news-item p{font-size:8.5px;color:var(--muted);line-height:1.35;margin-top:2px}
.news-item .more{color:var(--green)}
.posts{width:210px;background:#f4f4f4}
.posts-head{background:var(--teal);color:var(--white);font-size:12px;text-align:center;padding:8px 0}
.post{padding:8px 10px 0;font-size:8.5px;color:var(--muted);line-height:1.35}
.post b{color:var(--ink)}
.post .when{color:var(--blue);font-size:8px}
.posts-more{text-align:right;font-size:8px;color:var(--muted);padding:10px 10px 0}

/* footer */
.site-footer{position:absolute;left:0;top:1003px;width:720px;height:197px;background:var(--footer)}
.footer-cols{display:flex;justify-content:space-between;padding-top:18px}
.footer-col h5{font-size:10.5px;color:var(--white);font-weight:600;margin-bottom:4px}
.footer-col h5.gap{margin-top:12px}
.footer-col li{list-style:none;font-size:8.5px;color:var(--footer-text);line-height:1.45}
.footer-bar{position:absolute;left:0;bottom:0;width:720px;height:26px;background:var(--footer-deep);font-size:7.5px;color:#777;line-height:26px}
</style>
</head>
<body>

<header class="site-header wrap">
  <div class="brand">
    <div class="brand-name"><span class="brand-dot"></span>KELVO</div>
    <div class="brand-tag">kind at heart</div>
  </div>
  <div class="topbar">
    <span class="phone">
      <svg width="10" height="10" viewBox="0 0 24 24"><path d="M6.6 10.8a15 15 0 0 0 6.6 6.6l2.2-2.2a1 1 0 0 1 1-.25 11.4 11.4 0 0 0 3.6.57 1 1 0 0 1 1 1V20a1 1 0 0 1-1 1A17 17 0 0 1 3 4a1 1 0 0 1 1-1h3.5a1 1 0 0 1 1 1c0 1.25.2 2.45.57 3.57a1 1 0 0 1-.25 1z" fill="#76b22c"/></svg>
      +49 (0)340-552817-0
    </span>
    <span>Contact us | Follow us on</span><span class="sq"></span>
  </div>
  <nav class="main-nav">
    <a class="active">Home</a><a>Bio Plastics</a><a>Marusten Technology</a><a>About Us</a><a>Career</a><a>Contact</a>
  </nav>
</header>

<section class="hero wrap" role="img" aria-label="Photo of a green riverside landscape with trees under a bright sky">
  <div class="hero-caption">
    <div class="kicker">YOUR CUSTOMERS DEMAND</div>
    <h2>BIODEGRADABLE PACKAGING</h2>
    <div class="cta">Want to know how to supply it?
      <svg width="12" height="12" viewBox="0 0 12 12"><circle cx="6" cy="6" r="6" fill="#76b22c"/><path d="M5 3.5 7.5 6 5 8.5" stroke="#fff" stroke-width="1.4" fill="none"/></svg>
    </div>
  </div>
</section>

<section class="welcome wrap">
  <h1>Welcome to Our Website Mainpage..</h1>
  <p>At KELVO we license our MARUSTEN® Technology with the ambition to make it the world's industry standard for the production of and innovation in the area of biopolymers.</p>
  <span class="btn">LEARN MORE</span>
</section>

<section class="features wrap">
  <article class="card">
    <div class="card-img" role="img" aria-label="Photo of green leaves in a glass bowl" style="background:linear-gradient(160deg,#e9f3f8,#7fb7d6 60%,#3c86b5)"></div>
    <h3>What type of bio plastic are you looking for? We have them all</h3>
    <p>Biodegradable, bio-based and hybrid grades for films, bags and moulded parts, ready for your line.</p>
  </article>
  <article class="card">
    <div class="card-img" role="img" aria-label="Photo of hands holding a young seedling in soil" style="background:linear-gradient(160deg,#f3efe8,#c7a98a 55%,#6f9a3a)"></div>
    <h3>MARUSTEN® Technology the new industry standard</h3>
    <p>A patented process that turns renewable feedstock into resins that run on standard equipment.</p>
  </article>
  <article class="card">
    <div class="card-img" role="img" aria-label="Photo of the earth globe in a blue sky" style="background:linear-gradient(160deg,#cfe6f7,#4c95d0 55%,#1e5f9c)"></div>
    <h3>Ready to get started? We have two types of licenses on offer</h3>
    <p>Choose a compounder licence or a technology licence and start producing greener pellets soon.</p>
  </article>
  <article class="card">
    <div class="card-img" role="img" aria-label="Photo of a businessman holding a large green leaf" style="background:linear-gradient(160deg,#f7f7f2,#c9dda0 55%,#6da62c)"></div>
    <h3>We're recruiting</h3>
    <p>We are looking for chemists, engineers and sales people who want to shape biopolymers.</p>
  </article>
</section>

<section class="lower wrap">
  <div class="news">
    <h2 class="section-title">Our latest thoughts and News</h2>
    <article class="news-item">
      <div class="news-thumb" role="img" aria-label="Photo of a green leaf close-up" style="background:linear-gradient(135deg,#9ccc4a,#3f7d1f)"></div>
      <div><h4>Donec scelerisque leo</h4><p>Our team took part in a packaging forum this month and shared early results on compostable film grades with converters from across Europe. <span class="more">Read more</span></p></div>
    </article>
    <article class="news-item">
      <div class="news-thumb" role="img" aria-label="Photo of a green sprout" style="background:linear-gradient(135deg,#c6e08a,#5f9a2a)"></div>
      <div><h4>Mauris neque massa</h4><p>New trials show that MARUSTEN® based bags keep their strength during storage and still break down fully under industrial composting. <span class="more">Read more</span></p></div>
    </article>
    <article class="news-item">
      <div class="news-thumb" role="img" aria-label="Photo of blue water drops" style="background:linear-gradient(135deg,#7fc0e6,#1f5f96)"></div>
      <div><h4>Phasellus felis dolor</h4><p>We welcome two new licensed compounders who will bring bio-based pellets to customers in food packaging and agriculture next year. <span class="more">Read more</span></p></div>
    </article>
  </div>
  <aside class="posts">
    <div class="posts-head">What we're Posting about</div>
    <div class="post"><b>KELVO news:</b> New film grade passes compost test at partner lab<br><span class="when">Posted on 2 hours ago</span></div>
    <div class="post"><b>Licensing:</b> Licence talks opened with two compounders in Asia this week<br><span class="when">Posted on 3 hours ago</span></div>
    <div class="post"><b>Events:</b> Visit our booth at the plastics fair and meet our engineers<br><span class="when">Posted on 4 hours ago</span></div>
    <div class="posts-more">View More Blog Post ›</div>
  </aside>
</section>

<footer class="site-footer">
  <div class="footer-cols wrap">
    <div class="footer-col">
      <h5>Bio Plastics</h5>
      <ul><li>Typical Applications</li><li>MARUSTEN Biodegradable</li><li>MARUSTEN Biobased</li><li>MARUSTEN Hybrid</li></ul>
    </div>
    <div class="footer-col">
      <h5>MARUSTEN Technology</h5>
      <ul><li>What makes MARUSTEN Different</li><li>How it Works</li><li>FAQ</li></ul>
    </div>
    <div class="footer-col">
      <h5>License Opportunities</h5>
      <ul><li>Become a Licensed Compounder</li><li>Become a Technology Licensee</li></ul>
      <h5 class="gap">Latest Thinking</h5>
    </div>
    <div class="footer-col">
      <h5>About Us</h5>
      <ul><li>KELVO at a glance</li><li>Our values</li><li>Brand Promise</li><li>Management</li><li>History</li></ul>
    </div>
    <div class="footer-col">
      <h5>Career</h5>
      <ul><li>Life at KELVO</li><li>Join us</li></ul>
      <h5 class="gap">Contact Us</h5>
      <ul><li>Disclaimer</li><li>Data Protection</li></ul>
    </div>
  </div>
  <div class="footer-bar"><div class="wrap">© 2013 KELVO Polymer Systems AG. MARUSTEN® and KELVO® are registered trademarks owned by KELVO Polymer Systems AG.</div></div>
</footer>

</body>
</html>
```